Redesign Of Flower Delivery Subscription Service Website

I need a revamped website of www.petal-rush.com

Please revamp current design using same content....

Target Market(s)

people who buy flowers. Brides, wedding planners, wedding photographer, married man, boyfriend, etc.

Industry/Entity Type

Florist

Number of Pages Required

5+ page

Colors

Designer to choose colors to be used in the design.

Requirements
Must have
• I need a revamped website of www.petal-rush.com
• Please revamp current design using same content....
Nice to have
Should not have

```html
<!DOCTYPE html>
<html lang="en">
<head>
<meta charset="utf-8">
<title>PetalRush – Monthly Flower Delivery</title>
<link href="https://fonts.googleapis.com/css2?family=Raleway:wght@400;500;600&family=Dancing+Script:wght@500&family=Roboto+Condensed:wght@400;700&family=Open+Sans:wght@400;600&display=swap" rel="stylesheet">
<style>
:root{
  --green:#8fd150;
  --green-dark:#6bbf3a;
  --green-band:#93d251;
  --orange:#f9a825;
  --ink:#222;
  --muted:#666;
  --card:#e9e8e9;
  --footer:#353535;
  --white:#fff;
}
*{margin:0;padding:0;box-sizing:border-box}
html,body{width:850px;height:1200px;overflow:hidden;background:var(--white);font-family:'Raleway',sans-serif;color:var(--ink)}
.page{position:relative;width:850px;height:1200px}

.topbar{position:absolute;top:0;left:0;width:850px;height:24px;border-bottom:1px solid #eee;font-family:'Open Sans',sans-serif;font-size:7px;color:#555}
.topbar .gift{position:absolute;left:56px;top:8px;display:flex;align-items:center;gap:6px}
.topbar .gift a{color:#e0584b;text-decoration:none}
.topbar .call{position:absolute;left:351px;top:7px;font-size:8.5px}
.topbar .call span{color:var(--green-dark)}
.topbar .login{position:absolute;left:642px;top:7px}

.header{position:absolute;top:24px;left:0;width:850px;height:66px}
.brand{position:absolute;left:50px;top:22px;display:flex;align-items:center;gap:7px;font-size:22px;font-weight:500;color:#444;letter-spacing:1px}
.brand .dot{width:12px;height:12px;border-radius:50%;background:var(--green)}
.nav{position:absolute;left:214px;top:28px;display:flex;gap:10.5px;font-size:8px;color:#777;letter-spacing:.1px}
.nav .active{color:#333;font-weight:600}

.hero{position:absolute;top:90px;left:0;width:850px;height:393px;background:linear-gradient(90deg,#f4f7fa 0%,#eef2f6 40%,#e9eef2 100%)}
.hero-photo{position:absolute;right:0;top:0;width:470px;height:393px;background:radial-gradient(ellipse at 60% 60%,#f19fb0 0%,#ef9cad 30%,#f3c3cd 60%,rgba(238,242,246,0) 85%)}
.hero-copy{position:absolute;left:62px;top:100px}
.hero-title{font-family:'Dancing Script',cursive;font-size:76px;color:var(--green);line-height:1}
.hero-sub{margin-top:14px;font-size:15.5px;color:#333}
.hero-price{font-size:22px;color:#333;margin-top:1px}
.hero-tags{position:absolute;left:108px;top:255px;display:flex;gap:13px}
.tag{height:25px;padding:0 14px;background:var(--green);color:var(--white);font-size:10px;line-height:25px;border-radius:1px}

.signup-band{position:absolute;top:483px;left:0;width:850px;height:76px;background:var(--green-band)}
.signup-band .lead{position:absolute;left:144px;top:19px;font-family:'Roboto Condensed',sans-serif;color:var(--white);font-size:15px;line-height:19px}
.signup-band .lead strong{font-size:18px;font-weight:700}
.field{position:absolute;background:rgba(255,255,255,.3);border:1px solid rgba(255,255,255,.5);color:var(--white);font-size:6.5px;font-style:italic;padding-left:9px;display:flex;align-items:center}
.btn{position:absolute;background:var(--orange);color:var(--white);font-size:8px;display:flex;align-items:center;justify-content:center}

.features{position:absolute;top:588px;left:49px;display:flex;gap:9px}
.feature{width:244px;height:384px;background:var(--card)}
.feature-photo{position:relative;height:192px;display:flex;align-items:center;justify-content:center;text-align:center;color:var(--white);font-size:20px;line-height:26px}
.feature-photo.shop-yellow{background:linear-gradient(135deg,#4d3b2b,#7a6a3a 50%,#3f3a33)}
.feature-photo.purple{background:linear-gradient(135deg,#4a4870,#6a5fa0 50%,#3a3950)}
.feature-photo.shop-tulip{background:linear-gradient(135deg,#5b4b3c,#6d5d48 50%,#3e4a32)}
.feature-body{padding:18px 14px 0;text-align:center;font-size:12.8px;line-height:15.6px;color:#111}
.feature-body p+p{margin-top:15px}
.feature-body b{font-weight:600}

.footer{position:absolute;top:1023px;left:0;width:850px;height:177px;background:var(--footer);border-top:4px solid var(--green);font-family:'Open Sans',sans-serif;color:#ddd}
.col{position:absolute;top:20px}
.col h4{font-size:9px;font-weight:600;color:var(--white);margin-bottom:8px}
.col p{font-size:6.8px;line-height:16px}
.col .mail{color:#4c6a2a}
.col .phone{display:flex;align-items:center;gap:5px;font-size:12px;color:var(--green-dark);margin-top:3px}
.col ul{list-style:none;font-size:6.8px;line-height:16px}
.col li::before{content:"•";color:var(--orange);margin-right:6px}
.divider{position:absolute;top:20px;width:1px;height:108px;background:#4a4a4a}
.copyright{position:absolute;left:303px;top:139px;font-size:7px;color:var(--white)}
.copyright span{color:#4c6a2a}
.legal{position:absolute;left:616px;top:138px;font-size:7px;color:var(--white);display:flex;gap:8px}
</style>
</head>
<body>
<div class="page">
  <div class="topbar">
    <div class="gift">
      <svg width="11" height="11" viewBox="0 0 24 24"><polygon points="12,2 15,9 22,9.5 16.5,14 18.5,21 12,17 5.5,21 7.5,14 2,9.5 9,9" fill="none" stroke="#c0392b" stroke-width="1.6"/></svg>
      A SPECIAL GIFT FOR YOUR FIRST ORDER! <a href="#">Read info&gt;</a>
    </div>
    <div class="call">MAKE A CALL US <span>+45 555 0142</span></div>
    <div class="login">LOGIN / REGISTER</div>
  </div>

  <header class="header">
    <div class="brand"><span class="dot"></span>PetalRush</div>
    <nav class="nav">
      <span class="active">HOME</span><span>HOW IT WORKS</span><span>DELIVERY AREAS</span><span>FRANCHISE</span><span>MY ACCOUNT</span><span>BLOG</span><span>FREE FLOWERS MONTHLY</span><span>CORPORATE ARRANGEMENTS</span><span>HELP</span>
    </nav>
  </header>

  <section class="hero">
    <div class="hero-photo" role="img" aria-label="Bouquet of pink ranunculus flowers"></div>
    <div class="hero-copy">
      <div class="hero-title">Always fresh</div>
      <div class="hero-sub">Beautiful Flower Arrangements Delivered Monthly</div>
      <div class="hero-price">Now only $69.95/MTH ($100 value)</div>
    </div>
    <div class="hero-tags"><span class="tag">Free wash</span><span class="tag">Free Delivery</span><span class="tag">Free upgrade</span></div>
  </section>

  <section class="signup-band">
    <div class="lead">Enter Your Email To<br><strong>Receive A Free Upgrade</strong></div>
    <div class="field" style="left:395px;top:22px;width:287px;height:26px">Your Email Address</div>
    <div class="btn" style="left:693px;top:22px;width:52px;height:26px">Submit</div>
  </section>

  <section class="features">
    <article class="feature">
      <div class="feature-photo shop-yellow" role="img" aria-label="Florist holding a bouquet of yellow flowers in her shop">SET IT AND<br>FORGET IT</div>
      <div class="feature-body">
        <p>PetalRush is a “SET IT and FORGET IT” subscription based flower delivery service.</p>
        <p>For an Amazing price PetalRush will hand deliver a gorgeous arrange-ment directly to anyone you want every month without you having to worry about it.</p>
      </div>
    </article>
    <article class="feature">
      <div class="feature-photo purple" role="img" aria-label="Close-up of purple flowers">BUT NEVER<br>FORGET AGAIN</div>
      <div class="feature-body">
        <p>When setting up your account, you can choose exact delivery dates for the months that have special days such as <b>your Anniversary, Birthday, Valentines Day and Mothers Day.</b></p>
        <p>You might forget but we won't, we have got ya covered!</p>
      </div>
    </article>
    <article class="feature">
      <div class="feature-photo shop-tulip" role="img" aria-label="Florist holding a basket of tulips">MAKING SOMEONE'S<br>DAY BETTER</div>
      <div class="feature-body">
        <p>Be the hero in that special someone's life each and every month.</p>
        <p><b>It feels good to make a difference in your loved ones day.</b></p>
      </div>
    </article>
  </section>

  <footer class="footer">
    <div class="col" style="left:119px">
      <h4>Contact Info</h4>
      <p>1400 Harbor Lane, Lemon Grove CA 91945</p>
      <p>Email: <span class="mail">hello@petalrush.com</span></p>
      <div class="phone">
        <svg width="10" height="10" viewBox="0 0 24 24"><path d="M6.6 10.8a15 15 0 0 0 6.6 6.6l2.2-2.2a1 1 0 0 1 1-.25 11.4 11.4 0 0 0 3.6.57 1 1 0 0 1 1 1V20a1 1 0 0 1-1 1A17 17 0 0 1 3 4a1 1 0 0 1 1-1h3.5a1 1 0 0 1 1 1c0 1.25.2 2.45.57 3.6a1 1 0 0 1-.25 1z" fill="#f08a24"/></svg>
        619-555-0187
      </div>
    </div>
    <div class="divider" style="left:312px"></div>
    <div class="col" style="left:329px">
      <h4>More Services</h4>
      <ul><li>Corporate Arrangements</li><li>Hotel Arrangements</li><li>Events</li><li>Weddings</li></ul>
    </div>
    <div class="divider" style="left:522px"></div>
    <div class="col" style="left:539px">
      <h4>Receive A Free Upgrade</h4>
    </div>
    <div class="field" style="left:539px;top:39px;width:140px;height:26px;background:#555;border-color:#555;color:#ccc">Your Email Address</div>
    <div class="btn" style="left:679px;top:39px;width:54px;height:26px">Submit</div>
    <div class="copyright"><span>Petal Rush - Monthly Flowers Delivery</span> Copyright 2018. All Rights Reserved.</div>
    <div class="legal"><span>Privacy Policy</span><span>Terms &amp; Conditions</span></div>
  </footer>
</div>
</body>
</html>
```